Hi,

I would like to have a invitation made for a party. exactly like the picture in the link below.

http://pinboardia.example/pin/529174603381046725/

However, Please change the colors into fun/ girly feeling. font can be different and size of the card should be the same

Name of the girl: RUBA
What: Bachelorette Party
Where:TIKO Boat
Dubai Coral Sails Club
When:7th of February 2013

No RSVP required. (so no need to put it)

```html
<!DOCTYPE html>
<html lang="en">
<head>
<meta charset="utf-8">
<title>Ruba's Bachelorette Party Invitation</title>
<link rel="stylesheet" href="https://fonts.googleapis.com/css2?family=Fredoka:wght@600;700&family=Abril+Fatface&family=Roboto+Slab:wght@700&display=swap">
<style>
  :root {
    --paper: #fdf0f5;
    --paper-glow: #ffffff;
    --paper-edge: #fbdde9;
    --fold: #f3bcd3;
    --magenta: #e0157f;
    --plum: #7b1c7d;
    --plum-deep: #6a1670;
    --white: #ffffff;
    --ornament: #9a3a92;
  }
  * { box-sizing: border-box; margin: 0; padding: 0; }
  html, body {
    width: 1200px;
    height: 560px;
    overflow: hidden;
    background: var(--paper);
  }
  .invitation {
    position: relative;
    width: 1200px;
    height: 560px;
    overflow: hidden;
    background: radial-gradient(ellipse at 48% 42%, var(--paper-glow) 0%, var(--paper) 55%, var(--paper-edge) 100%);
  }
  .fold {
    position: absolute;
    top: 0;
    width: 1px;
    height: 560px;
    background: var(--fold);
  }
  .fold--first { left: 400px; }
  .fold--second { left: 800px; }

  .corner-ornament {
    position: absolute;
    width: 68px;
    height: 68px;
    background: linear-gradient(135deg, var(--ornament), rgba(154, 58, 146, 0.15));
    opacity: 0.55;
  }
  .corner-ornament--top {
    left: 310px;
    top: 24px;
    clip-path: polygon(0 0, 100% 0, 100% 100%, 86% 100%, 86% 14%, 0 14%);
  }
  .corner-ornament--bottom {
    left: 22px;
    top: 468px;
    clip-path: polygon(0 0, 14% 0, 14% 86%, 100% 86%, 100% 100%, 0 100%);
  }

  .headline {
    position: absolute;
    left: 0;
    top: 0;
    width: 800px;
    height: 560px;
  }
  .bride-name {
    font-family: "Fredoka", sans-serif;
    font-weight: 700;
    fill: var(--magenta);
  }
  .tagline {
    font-family: "Abril Fatface", serif;
    fill: var(--plum);
  }
  .single-word {
    font-family: "Fredoka", sans-serif;
    font-weight: 700;
  }
  .single-word--outer { stroke: var(--plum); stroke-width: 20px; stroke-linejoin: round; fill: var(--plum); }
  .single-word--inner { stroke: var(--white); stroke-width: 9px; stroke-linejoin: round; fill: var(--white); }

  .divider {
    position: absolute;
    left: 447px;
    top: 186px;
    width: 306px;
    height: 44px;
  }
  .divider-flourish {
    position: absolute;
    left: 114px;
    top: 0;
    width: 70px;
    height: 32px;
    background: linear-gradient(180deg, var(--magenta), rgba(224, 21, 127, 0.35));
    opacity: 0.7;
    clip-path: polygon(50% 0, 100% 80%, 60% 100%, 40% 100%, 0 80%);
  }

  .details-frame {
    position: absolute;
    left: 832px;
    top: 58px;
    width: 336px;
    height: 446px;
    background: linear-gradient(160deg, var(--ornament), var(--plum-deep));
    opacity: 0.9;
  }
  .details-card {
    position: absolute;
    left: 860px;
    top: 84px;
    width: 280px;
    height: 394px;
    background: var(--white);
    font-family: "Roboto Slab", serif;
    font-weight: 700;
    text-align: center;
  }
  .detail {
    position: absolute;
    left: 0;
    width: 100%;
  }
  .detail--name { top: 42px; }
  .detail--what { top: 122px; }
  .detail--where { top: 208px; }
  .detail--when { top: 312px; }
  .detail-label {
    color: var(--plum);
    font-size: 13.5px;
    line-height: 20px;
  }
  .detail-value {
    color: var(--magenta);
    font-size: 15px;
    line-height: 22px;
  }
</style>
</head>
<body>
<main class="invitation">
  <div class="fold fold--first"></div>
  <div class="fold fold--second"></div>

  <div class="corner-ornament corner-ornament--top" role="img" aria-label="Purple floral corner ornament"></div>
  <div class="corner-ornament corner-ornament--bottom" role="img" aria-label="Purple floral corner ornament"></div>

  <svg class="headline" viewBox="0 0 800 560" aria-label="Ruba's last chance to celebrate being single">
    <defs>
      <linearGradient id="single-fill" x1="0" y1="0" x2="0" y2="1">
        <stop offset="0" stop-color="#7b1c7d"/>
        <stop offset="0.55" stop-color="#b01a80"/>
        <stop offset="1" stop-color="#e0157f"/>
      </linearGradient>
    </defs>

    <text class="bride-name" x="34" y="230" font-size="112" textLength="300" lengthAdjust="spacingAndGlyphs">RUBA</text>
    <path class="bride-heart" fill="var(--magenta)" d="M303 150c-3-7-14-6-14 2 0 6 8 10 14 16 6-6 14-10 14-16 0-8-11-9-14-2z" transform="translate(40 0)"/>
    <text class="bride-name" x="366" y="230" font-size="112">S</text>

    <text class="tagline" x="34" y="305" font-size="74" textLength="752" lengthAdjust="spacingAndGlyphs">LAST CHANCE TO CELEBRATE BEING</text>

    <text class="single-word single-word--outer" x="40" y="468" font-size="190" textLength="735" lengthAdjust="spacingAndGlyphs">SiNGLE</text>
    <text class="single-word single-word--inner" x="40" y="468" font-size="190" textLength="735" lengthAdjust="spacingAndGlyphs">SiNGLE</text>
    <text class="single-word" x="40" y="468" font-size="190" textLength="735" lengthAdjust="spacingAndGlyphs" fill="url(#single-fill)">SiNGLE</text>
  </svg>

  <div class="divider">
    <svg width="306" height="44" viewBox="0 0 306 44" aria-hidden="true">
      <path d="M0 35 L108 33.5 L108 36.5 Z" fill="var(--magenta)"/>
      <path d="M306 35 L198 33.5 L198 36.5 Z" fill="var(--magenta)"/>
      <rect x="100" y="31" width="6" height="6" transform="rotate(45 103 34)" fill="var(--magenta)"/>
      <rect x="200" y="31" width="6" height="6" transform="rotate(45 203 34)" fill="var(--magenta)"/>
    </svg>
    <div class="divider-flourish" role="img" aria-label="Magenta scroll flourish centrepiece"></div>
  </div>

  <div class="details-frame" role="img" aria-label="Ornate purple scrollwork frame"></div>
  <section class="details-card">
    <div class="detail detail--name">
      <p class="detail-label">Name of the girl:</p>
      <p class="detail-value">RUBA</p>
    </div>
    <div class="detail detail--what">
      <p class="detail-label">What:</p>
      <p class="detail-value">Bachelorette Party</p>
    </div>
    <div class="detail detail--where">
      <p class="detail-label">Where:</p>
      <p class="detail-value">TIKO Boat</p>
      <p class="detail-value">Dubai Coral Sails Club</p>
    </div>
    <div class="detail detail--when">
      <p class="detail-label">When:</p>
      <p class="detail-value">7th of February 2013</p>
    </div>
  </section>
</main>
</body>
</html>
```